Exercise Physiologist needs business cards

I have a logo, I need business cards (Sole trader) as I am moving to a new location and would like an updated look. I provide gym based exercise rehabilitation, injury prevention and movement assessments. I have over 13 years experience as an Exercise Physiologist. I would like the cards to look professional but not boring and can be a little different to stand out when sitting with other Allied Health Professional cards.

Target Market(s)

GP's, Allied health practitioners, people with injuries wanting to exercise

Industry/Entity Type

Health And Wellness

Contact Information for Business Card

Megan Dorrit - Exercise Physiologist 0437 582 906
14 Larkspur Bend Rd
Port Ellery
(Gate 4, Brannock Fitness)
vantorahealth@maildrop-example.com
socialpage-example.com/Vantora

Requirements
Must have
• I would like to include a section to add next appointment date and time space to the back of the card.
Nice to have
• Rounded corners and a black background on 1 or 2 sides.
Should not have
• Pictures of fit/toned bodies etc

```html
<!DOCTYPE html>
<html lang="en">
<head>
<meta charset="utf-8">
<title>Vantora Health &amp; Rehabilitation – Business Card</title>
<link href="https://fonts.googleapis.com/css2?family=Montserrat:wght@400;500;700&display=swap" rel="stylesheet">
<style>
  :root {
    --page-bg: #d9d9d9;
    --card-bg: #222222;
    --card-bg-edge: #1a1a1a;
    --brand-blue: #2f6ad0;
    --accent-blue: #4aa6e6;
    --field-bg: #f2f2f2;
    --field-line: #8a8a8a;
    --field-text: #6d6d6d;
  }
  * { box-sizing: border-box; margin: 0; padding: 0; }
  html, body {
    width: 1200px; height: 900px; overflow: hidden;
    background: var(--page-bg);
    font-family: "Montserrat", sans-serif;
  }
  .stage {
    width: 1200px; height: 900px;
    display: flex; align-items: center; justify-content: center; gap: 90px;
  }
  .card {
    position: relative;
    width: 380px; height: 640px;
    border-radius: 32px;
    background: radial-gradient(ellipse at 50% 40%, var(--card-bg) 0%, var(--card-bg-edge) 100%);
    box-shadow: 0 18px 40px rgba(0,0,0,0.25);
    color: var(--brand-blue);
  }

  /* Front */
  .holder { position: absolute; top: 56px; left: 40px; }
  .holder-name {
    font-weight: 700; font-size: 26px; letter-spacing: 1.5px;
    text-transform: uppercase; color: var(--brand-blue);
  }
  .holder-title {
    margin-top: 4px; font-weight: 400; font-size: 15px; letter-spacing: 1px;
    text-transform: uppercase; color: var(--accent-blue);
  }
  .holder-rule {
    margin-top: 12px; width: 24px; height: 3px; background: var(--accent-blue);
  }

  .brand {
    position: absolute; left: 0; right: 0;
    display: flex; flex-direction: column; align-items: center;
  }
  .card-front .brand { top: 250px; }
  .card-back .brand { top: 210px; }
  .brand-dot {
    width: 70px; height: 70px; border-radius: 50%;
    background: var(--accent-blue);
  }
  .brand-name {
    margin-top: 14px;
    font-weight: 500; font-size: 46px; letter-spacing: 1px;
    color: var(--brand-blue); line-height: 1;
  }
  .brand-tagline {
    margin-top: 8px;
    font-weight: 400; font-size: 12px; letter-spacing: 1px;
    text-transform: uppercase; color: var(--brand-blue);
  }

  .contact {
    position: absolute; right: 34px; bottom: 48px;
    list-style: none; text-align: right;
    font-size: 14px; line-height: 1.6; color: var(--accent-blue);
  }
  .contact-tag { color: var(--brand-blue); margin-left: 3px; }

  /* Back */
  .appointment {
    position: absolute; left: 40px; right: 40px; top: 410px;
    text-align: center;
  }
  .appointment-label {
    font-size: 13px; font-weight: 500; letter-spacing: 3px;
    text-transform: uppercase; color: var(--accent-blue);
  }
  .appointment-field {
    margin-top: 12px; height: 56px; border-radius: 8px;
    background: var(--field-bg);
    box-shadow: inset 0 0 0 2px #ffffff, 0 2px 6px rgba(0,0,0,0.4);
    display: flex; align-items: center; gap: 18px; padding: 0 18px;
    font-size: 14px; color: var(--field-text);
  }
  .field-entry { flex: 1; display: flex; align-items: flex-end; gap: 4px; }
  .field-line { flex: 1; border-bottom: 1px solid var(--field-line); height: 14px; }
</style>
</head>
<body>
<main class="stage">

  <section class="card card-front" aria-label="Business card front">
    <header class="holder">
      <h1 class="holder-name">Megan Dorrit</h1>
      <p class="holder-title">Exercise Physiologist</p>
      <div class="holder-rule"></div>
    </header>

    <div class="brand">
      <div class="brand-dot"></div>
      <div class="brand-name">vantora</div>
      <div class="brand-tagline">Health &amp; Rehabilitation</div>
    </div>

    <ul class="contact">
      <li>0437 582 906<span class="contact-tag">[T]</span></li>
      <li>vantorahealth@maildrop-example.com<span class="contact-tag">[E]</span></li>
      <li>socialpage-example.com/Vantora<span class="contact-tag">[F]</span></li>
      <li>14 Larkspur Bend Rd<span class="contact-tag">[A]</span></li>
      <li>Port Ellery</li>
      <li>(Gate 4, Brannock Fitness)</li>
    </ul>
  </section>

  <section class="card card-back" aria-label="Business card back">
    <div class="brand">
      <div class="brand-dot"></div>
      <div class="brand-name">vantora</div>
      <div class="brand-tagline">Health &amp; Rehabilitation</div>
    </div>

    <div class="appointment">
      <p class="appointment-label">Appointment</p>
      <div class="appointment-field">
        <span class="field-entry">Date:<span class="field-line"></span></span>
        <span class="field-entry">Time:<span class="field-line"></span></span>
      </div>
    </div>
  </section>

</main>
</body>
</html>
```